Welding company needs a business card

We are looking for a logo and business card.

Contact Information for Business Card

418 Cobblestone Lane
York, PA 17402
410-555-0173
Rmfabworksco@quorvamail.com

```html
<!DOCTYPE html>
<html lang="en">
<head>
<meta charset="utf-8">
<title>RM Fabworks Company – Business Card</title>
<link rel="stylesheet" href="https://fonts.googleapis.com/css2?family=Open+Sans:wght@400;700;800&display=swap">
<style>
  :root {
    --navy: #0b0b77;
    --red: #ea3237;
    --ink: #353535;
    --frame: #3a3a3a;
    --ghost: #dcdbe6;
    --paper: #ffffff;
  }
  * { margin: 0; padding: 0; box-sizing: border-box; }
  html, body { width: 1200px; height: 687px; overflow: hidden; background: var(--paper); }
  .card {
    position: relative;
    width: 1200px; height: 687px;
    background: var(--paper);
    border: 2px solid var(--frame);
    overflow: hidden;
    font-family: "Open Sans", sans-serif;
  }
  .card-art { position: absolute; inset: 0; }
  .brand {
    position: absolute;
    left: 84px; top: 358px;
    width: 430px;
    color: var(--navy);
    font-weight: 800;
    font-size: 50px;
    line-height: 1;
    white-space: nowrap;
  }
  .brand-line { display: block; }
  .brand-line + .brand-line { margin-top: 10px; }
  .contact {
    position: absolute;
    left: 672px; top: 406px;
    list-style: none;
    color: var(--ink);
    white-space: nowrap;
  }
  .contact-item {
    position: relative;
    padding-left: 62px;
    line-height: 1.2;
  }
  .contact-icon {
    position: absolute; left: 0; top: 3px;
    width: 38px; height: 38px;
  }
  .contact-phone { font-size: 35px; font-weight: 700; }
  .contact-email { font-size: 28px; font-weight: 400; margin-top: 6px; }
  .contact-email .contact-icon { top: 0; }
  .contact-address { font-size: 34px; font-weight: 700; margin-top: 10px; line-height: 1.22; }
</style>
</head>
<body>
<div class="card">
  <svg class="card-art" width="1200" height="687" viewBox="0 0 1200 687" aria-hidden="true">
    <circle class="ghost-ring" cx="-10" cy="-70" r="180" fill="none" stroke="var(--ghost)" stroke-width="42"/>
    <circle class="ghost-ring" cx="1085" cy="60" r="225" fill="none" stroke="var(--ghost)" stroke-width="46" opacity="0.7"/>
    <circle class="brand-dot" cx="296" cy="206" r="134" fill="var(--navy)"/>
    <polygon class="band-red" points="0,620 597,620 540,687 0,687" fill="var(--red)"/>
    <polygon class="band-navy" points="625,620 1200,620 1200,687 571,687" fill="var(--navy)"/>
  </svg>

  <div class="brand">
    <span class="brand-line">RM FABWORKS</span>
    <span class="brand-line">COMPANY</span>
  </div>

  <ul class="contact">
    <li class="contact-item contact-phone">
      <svg class="contact-icon" viewBox="0 0 38 38" aria-hidden="true">
        <circle cx="19" cy="19" r="19" fill="var(--navy)"/>
        <path d="M13 10c1-1 2-1 3 0l2 3c.6 1 .3 2-.5 2.6l-1 .8c.8 2 2.4 3.7 4.3 4.6l.9-1c.7-.8 1.7-1 2.6-.4l3 2c1 .7 1 1.8.2 2.7l-1.3 1.4c-1.5 1.5-4 1.3-6.6-.4-3-2-5.6-4.8-7-8-1.2-2.8-1.1-5.6.1-7.3z" fill="none" stroke="#fff" stroke-width="1.8"/>
        <path d="M21 11a6 6 0 0 1 6 6M21 7.5a9.5 9.5 0 0 1 9.5 9.5" fill="none" stroke="#fff" stroke-width="1.6" stroke-linecap="round"/>
      </svg>
      410-555-0173
    </li>
    <li class="contact-item contact-email">
      <svg class="contact-icon" viewBox="0 0 38 38" aria-hidden="true">
        <circle cx="19" cy="19" r="19" fill="var(--navy)"/>
        <rect x="9" y="12" width="20" height="14" fill="none" stroke="#fff" stroke-width="2"/>
        <path d="M9 12l10 8 10-8M9 26l7-7M29 26l-7-7" fill="none" stroke="#fff" stroke-width="2"/>
      </svg>
      Rmfabworksco@quorvamail.com
    </li>
    <li class="contact-item contact-address">
      <svg class="contact-icon" viewBox="0 0 38 38" aria-hidden="true">
        <circle cx="19" cy="19" r="19" fill="var(--navy)"/>
        <path d="M19 30c-4-5-7-9-7-13a7 7 0 0 1 14 0c0 4-3 8-7 13z" fill="#fff"/>
        <circle cx="19" cy="17" r="2.6" fill="var(--navy)"/>
      </svg>
      418 Cobblestone Lane<br>York, PA 17402
    </li>
  </ul>
</div>
</body>
</html>
```